BrovaLT BIZ Card, email signature & Stationary

Professional business cards, email signatures and ms word letterhead

Target Market(s)

business owners

Industry/Entity Type

cloud hosting

Contact Information for Business Card

name title office phone number , direct line, fax email address web site

Font styles to use
Other font styles liked:
• something that compliments font in logo

```html
<!DOCTYPE html>
<html lang="en">
<head>
<meta charset="utf-8">
<title>BrovaLT Business Card</title>
<link rel="stylesheet" href="https://fonts.googleapis.com/css2?family=Montserrat:wght@300;400;600;700&display=swap">
<style>
  :root {
    --bg: #b9b9b9;
    --card: #1f1f1f;
    --red: #e8161f;
    --white: #ffffff;
    --text: #f2f2f2;
  }
  * { margin: 0; padding: 0; box-sizing: border-box; }
  html, body { width: 1200px; height: 802px; overflow: hidden; }
  body {
    background: linear-gradient(180deg, #d3d3d3 0%, var(--bg) 100%);
    font-family: "Montserrat", sans-serif;
    position: relative;
  }
  .card {
    position: absolute;
    width: 520px;
    height: 298px;
    background: var(--card);
    border-radius: 22px;
    overflow: hidden;
    box-shadow: 0 14px 30px rgba(0,0,0,0.35);
  }
  .card-front { left: 50px; top: 252px; }
  .card-back  { left: 630px; top: 252px; }

  .brand {
    position: absolute;
    font-weight: 300;
    color: var(--red);
    letter-spacing: 1px;
    white-space: nowrap;
  }
  .card-front .brand { right: 58px; top: 44px; font-size: 58px; }
  .card-back .brand {
    left: 0; right: 0; top: 100px;
    text-align: center;
    font-size: 84px;
  }

  .divider {
    position: absolute;
    left: 40px; right: 40px; top: 150px;
    height: 1px;
    background: var(--red);
    opacity: 0.85;
  }

  .person { position: absolute; left: 40px; top: 110px; }
  .person-name {
    color: var(--red);
    font-weight: 700;
    font-size: 17px;
    letter-spacing: 0.5px;
  }
  .person-title {
    color: var(--text);
    font-weight: 400;
    font-size: 13px;
    margin-top: 2px;
  }

  .contact-list {
    position: absolute;
    list-style: none;
    color: var(--text);
    font-size: 13px;
    font-weight: 400;
  }
  .contact-list li { display: flex; align-items: center; gap: 8px; height: 20px; }
  .contact-list svg { width: 12px; height: 12px; flex: none; }
  .phones { left: 40px; top: 166px; }
  .online { right: 40px; top: 176px; }

  .edge-band {
    position: absolute;
    left: 0; right: 0; bottom: 0;
    height: 14px;
  }
</style>
</head>
<body>

  <section class="card card-front" aria-label="Business card front">
    <div class="brand">BrovaLT</div>

    <div class="person">
      <div class="person-name">DANA KELLER</div>
      <div class="person-title">CEO/Founder</div>
    </div>

    <div class="divider"></div>

    <ul class="contact-list phones">
      <li>
        <svg viewBox="0 0 12 12"><path d="M2.5 1 L4.5 1 L5.2 3.6 L3.9 4.6 C4.6 6 5.9 7.3 7.4 8.1 L8.4 6.8 L11 7.5 L11 9.5 C11 10.3 10.3 11 9.5 11 C5 11 1 7 1 2.5 C1 1.7 1.7 1 2.5 1 Z" fill="var(--red)"/></svg>
        (888) 555-0142
      </li>
      <li>
        <svg viewBox="0 0 12 12"><rect x="3" y="0.8" width="6" height="10.4" rx="1" fill="none" stroke="var(--red)" stroke-width="1.3"/><circle cx="6" cy="9.2" r="0.7" fill="var(--red)"/></svg>
        (987) 555-0176
      </li>
      <li>
        <svg viewBox="0 0 12 12"><rect x="3" y="1" width="6" height="3" fill="var(--red)"/><rect x="1" y="4.5" width="10" height="4.5" rx="1" fill="var(--red)"/><rect x="3" y="8" width="6" height="3" fill="var(--card)" stroke="var(--red)" stroke-width="1"/></svg>
        1-888-555-0163
      </li>
    </ul>

    <ul class="contact-list online">
      <li>
        <svg viewBox="0 0 12 12"><rect x="0.5" y="2.5" width="11" height="7" fill="var(--red)"/><path d="M0.5 2.5 L6 6.5 L11.5 2.5" fill="none" stroke="var(--card)" stroke-width="1"/></svg>
        info@brovalt.com
      </li>
      <li>
        <svg viewBox="0 0 12 12"><circle cx="6" cy="6" r="5.2" fill="var(--red)"/><path d="M0.8 6 H11.2 M6 0.8 V11.2 M2 3.5 H10 M2 8.5 H10" stroke="var(--card)" stroke-width="0.7" fill="none"/></svg>
        www.brovalt.com
      </li>
    </ul>

    <svg class="edge-band" viewBox="0 0 520 14" preserveAspectRatio="none" aria-hidden="true">
      <polygon points="0,6 250,6 244,14 0,14" fill="var(--red)"/>
      <polygon points="256,0 520,0 520,14 248,14" fill="var(--white)"/>
    </svg>
  </section>

  <section class="card card-back" aria-label="Business card back">
    <div class="brand">BrovaLT</div>
  </section>

</body>
</html>
```